International gym review site. Needs a full website frontend (mobile + desktop) designing and a logo

Our UK based business 'LiftHarbor' is launching its international review website for independent and hotel gyms. Our website will be a fresh, funky and clean version of Wandernote but for gyms.
We require the designs in sketch, psd, illustrator

We would like to see clean designs that incorporate gym style icons. We also require our logo designing which will need to complement the design of the site. We have included wireframes of how we envisage the site coming together. However, we are very flexible on this and have nothing set in stone.

We would like the designs to mobile first focused with desktop experince being the latter (although we have wireframed for desktop - we are very open to ideas and suggestions)

Please find below a number of websites that we like and have found inspiration from:

- https://www.ledgrova.example/uk/
- chatrumble.example
- Map is cool on here https://pinroster.bykelvane.example/
- Looks cool like roof n'stay (listing section could be smaller) -https://quillmarsh.example/demos/themes/?product=rowvane
- Like this but needs to be more compact https://catalo-demos.brimvexa.example/rentals/listing/private-bedroom-w-bathroom/
- Like the homepage of this one https://entrypath.dorvix.example/
- https://www.trevolo.example.co.uk/hotels - looks clean, like the layout of this especially the hotel section
- https://www.trevolo.example.co.uk/Barcelona-Hotels.48213.hotel.ksp - the good to know section is good
- https://bytewire.example/2017/10/20/streamvo-unveils-a-suite-of-new-tools-to-help-creators-grow-their-channels-and-make-money/
- https://www.quietlodgings.example/
- https://www.motorbazel.example.co.uk

Target Market(s)

Fitness users and hotel goers who want to use a gym. Generally affluent aged 20-50years old of multi-nationalities

Industry/Entity Type

Fitness

Logo Text

LiftHarbor (optional)

Number of Pages Required

5+ page

Colors

Designer to choose colors to be used in the design.

Requirements
Must have
• Clean, flat minimal, pleasing on the eye.
• Bright / colourful
• Clean fonts (no specific font picked, will leave colour palette and fonts to the designer)
Should not have
• Cluttered and disorganised feel.
• Dark and dreary.

```html
<!DOCTYPE html>
<html lang="en">
<head>
<meta charset="utf-8">
<title>LiftHarbor – Hotel &amp; Independent Gyms</title>
<link rel="stylesheet" href="https://fonts.googleapis.com/css2?family=Open+Sans:wght@400;600;700&display=swap">
<style>
:root{
  --teal:#1f9c8f;
  --teal-dark:#167a70;
  --teal-slate:#2f8190;
  --ink:#3e4347;
  --muted:#8d9398;
  --page:#eef0f2;
  --white:#ffffff;
  --map:#5f6366;
  --footer:#24272b;
  --footer-bottom:#1b1d20;
  --footer-text:#a6abb0;
}
*{box-sizing:border-box;margin:0;padding:0}
html,body{width:1200px;height:2944px;overflow:hidden}
body{font-family:"Open Sans",Arial,sans-serif;background:var(--page);color:var(--ink);position:relative}
a{color:inherit;text-decoration:none}

/* header */
.site-header{position:absolute;top:0;left:0;width:1200px;height:64px;background:var(--white);display:flex;align-items:center}
.brand{position:absolute;left:26px;top:10px;display:flex;align-items:center;gap:8px;font-size:13px;font-weight:600;color:var(--muted)}
.brand-mark{width:30px;height:30px;border:2px solid var(--muted);border-radius:50%}
.main-nav{position:absolute;left:364px;top:18px;display:flex;gap:8px}
.main-nav a{font-size:15px;color:var(--ink);padding:4px 12px;border:1px solid transparent;border-radius:3px}
.main-nav a.is-active{border-color:var(--teal);color:var(--teal)}
.user-btn{position:absolute;right:56px;top:12px;width:44px;height:40px;background:var(--teal);border-radius:4px;display:flex;align-items:center;justify-content:center}

/* hero */
.hero{position:absolute;top:64px;left:0;width:1200px;height:736px;background:linear-gradient(180deg,#6c7073,#55595c 70%,#4b4f52);overflow:hidden}
.hero-map{position:absolute;inset:0}
.hero-card{position:absolute;left:404px;top:276px;width:392px;height:454px;background:var(--teal);color:var(--white);text-align:center;padding:44px 40px;box-shadow:0 10px 30px rgba(0,0,0,.25)}
.hero-card h1{font-size:30px;font-weight:600;letter-spacing:1px}
.hero-card hr{border:0;border-top:1px solid rgba(255,255,255,.6);margin:26px 0 20px}
.hero-card .city{font-size:15px;font-weight:600;letter-spacing:1px}
.hero-card p{font-size:12px;line-height:1.5;margin-top:16px;opacity:.9}
.hero-card .cta{display:inline-block;margin-top:42px;border:2px solid var(--white);padding:16px 34px;font-size:15px;font-weight:600;letter-spacing:2px}

/* intro */
.intro{position:absolute;top:830px;left:0;width:1200px;text-align:center}
.intro h2{font-size:38px;font-weight:400;color:var(--ink)}
.intro h2 strong{font-weight:600}
.intro p{width:840px;margin:22px auto 0;font-size:17px;line-height:1.45;color:var(--muted)}

/* listings */
.listings{position:absolute;top:1000px;left:64px;width:1072px;height:1212px;background:var(--white);padding-top:20px}
.section-title{text-align:center;font-size:36px;font-weight:400;letter-spacing:2px;color:var(--ink)}
.card-row{display:flex;gap:40px;justify-content:center;margin-top:28px}
.gym-card{width:456px;text-align:center}
.gym-photo{position:relative;height:200px}
.gym-photo .fill{position:absolute;inset:0}
.rating{position:absolute;right:-4px;bottom:-34px;width:60px;height:60px;border-radius:50%;background:var(--teal);border:4px solid var(--white);color:var(--white);font-weight:600;font-size:20px;display:flex;align-items:center;justify-content:center}
.gym-card h3{margin-top:28px;font-size:15px;font-weight:600;letter-spacing:1px;color:var(--ink)}
.gym-card p{margin:14px auto 0;width:400px;font-size:13px;line-height:1.6;color:var(--muted)}
.see-more{display:block;width:192px;height:44px;margin:42px auto 0;background:var(--teal-slate);color:var(--white);font-size:14px;font-weight:600;letter-spacing:1px;line-height:44px;text-align:center}
.block-2{margin-top:40px}

/* partners */
.partners{position:absolute;top:2238px;left:0;width:1200px;height:170px;display:flex;align-items:center;justify-content:center}
.partners .arrow{position:absolute;top:70px}
.partners .arrow.left{left:34px}
.partners .arrow.right{right:34px}
.partner-list{display:flex;gap:60px;align-items:center}
.partner{display:flex;align-items:center;gap:10px;font-size:24px;font-weight:700;color:var(--teal-dark)}
.partner .dot{width:24px;height:24px;border-radius:50%;background:var(--teal)}

/* footer */
.site-footer{position:absolute;top:2426px;left:0;width:1200px;height:518px;background:var(--footer);color:var(--footer-text)}
.footer-cols{display:flex;padding:90px 0 0 84px}
.footer-col h4{color:var(--white);font-size:15px;font-weight:700;letter-spacing:1px;margin-bottom:40px}
.col-contact{width:264px}
.col-links{width:262px}
.col-posts{width:266px}
.contact-item{display:flex;gap:16px;margin-bottom:30px;font-size:13px;line-height:1.5}
.contact-item .ico{width:26px;height:26px;background:var(--teal);border-radius:3px;flex:none;display:flex;align-items:center;justify-content:center}
.col-links li{list-style:none;font-size:13px;line-height:22px}
.post{display:flex;gap:14px;margin-bottom:30px}
.post .thumb{width:64px;height:64px;background:linear-gradient(135deg,#7a6a5a,#3d3a38)}
.post p{font-size:13px;line-height:1.45;width:140px}
.post time{display:block;color:var(--teal);font-size:12px;margin-top:2px}
.gallery{display:grid;grid-template-columns:repeat(3,62px);gap:8px}
.gallery span{height:52px;display:block}
.footer-bottom{position:absolute;bottom:0;left:0;width:1200px;height:70px;background:var(--footer-bottom);text-align:center;line-height:70px;font-size:12px}
</style>
</head>
<body>

<header class="site-header">
  <div class="brand"><span class="brand-mark"></span>LiftHarbor</div>
  <nav class="main-nav">
    <a class="is-active" href="#">Home</a>
    <a href="#">Explore</a>
    <a href="#">Destinations ▾</a>
    <a href="#">Pages</a>
    <a href="#">Blogs</a>
    <a href="#">Contact</a>
  </nav>
  <a class="user-btn" href="#" aria-label="Account">
    <svg width="20" height="20" viewBox="0 0 20 20"><circle cx="10" cy="6" r="4" fill="#fff"/><path d="M2 19c0-5 4-7 8-7s8 2 8 7z" fill="#fff"/></svg>
  </a>
</header>

<section class="hero">
  <div class="hero-map" role="img" aria-label="World map with location pins marking gyms"></div>
  <svg class="hero-map" width="1200" height="736" viewBox="0 0 1200 736" aria-hidden="true">
    <g fill="#b52a2a">
      <path d="M432 0a16 16 0 0 1 16 16c0 12-16 28-16 28s-16-16-16-28a16 16 0 0 1 16-16z"/>
      <path d="M232 100a14 14 0 0 1 14 14c0 10-14 24-14 24s-14-14-14-24a14 14 0 0 1 14-14z"/>
      <path d="M836 66a28 28 0 0 1 28 28c0 22-28 52-28 52s-28-30-28-52a28 28 0 0 1 28-28z"/>
      <path d="M742 92a12 12 0 0 1 12 12c0 9-12 20-12 20s-12-11-12-20a12 12 0 0 1 12-12z"/>
    </g>
    <g fill="#27a596">
      <path d="M1026 0a14 14 0 0 1 14 14c0 10-14 24-14 24s-14-14-14-24a14 14 0 0 1 14-14z"/>
      <path d="M346 522a14 14 0 0 1 14 14c0 10-14 24-14 24s-14-14-14-24a14 14 0 0 1 14-14z"/>
    </g>
  </svg>
  <div class="hero-card">
    <h1>LiftHarbor</h1>
    <hr>
    <div class="city">BARCELONA</div>
    <p>Find top gyms by city. Honest reviews from members and hotel guests. Compare kit, classes, hours and day pass prices before you travel.</p>
    <a class="cta" href="#">TELL ME MORE</a>
  </div>
</section>

<section class="intro">
  <h2>The Best Luxury <strong>Hotel Gyms</strong></h2>
  <p>Lorem Ipsum is simply dummy text of the printing and typesetting industry. Lorem Ipsum has been the industry's standard dummy text ever since the 1500s, when an unknown printer took a galley of type and scrambled it to make a type specimen book.</p>
</section>

<main class="listings">
  <h2 class="section-title">HOTEL GYMS</h2>
  <div class="card-row">
    <article class="gym-card">
      <div class="gym-photo"><div class="fill" role="img" aria-label="Hotel gym interior with rows of cardio machines" style="background:linear-gradient(180deg,#d6d9db,#8a8f93 60%,#5d6166)"></div><span class="rating">4.7</span></div>
      <h3>BARCELONA</h3>
      <p>Sed tristique purus vitae volutpat commodo suscipit amet sed nibh. Proin a ullamcorper sed blandit. Sed tristique purus vitae volutpat commodo suscipit a ullamcorper sed blandit lorem ipsum dolore.</p>
    </article>
    <article class="gym-card">
      <div class="gym-photo"><div class="fill" role="img" aria-label="Hotel gym with weight machines and red flooring" style="background:linear-gradient(180deg,#c8b9a4,#6f5a48 55%,#8c2a24)"></div><span class="rating">4.7</span></div>
      <h3>BARCELONA</h3>
      <p>Sed tristique purus vitae volutpat commodo suscipit amet sed nibh. Proin a ullamcorper sed blandit. Sed tristique purus vitae volutpat commodo suscipit a ullamcorper sed blandit lorem ipsum dolore.</p>
    </article>
  </div>
  <a class="see-more" href="#">SEE MORE</a>

  <div class="block-2">
    <h2 class="section-title">INDEPENDENT GYMS</h2>
    <div class="card-row">
      <article class="gym-card">
        <div class="gym-photo"><div class="fill" role="img" aria-label="Independent gym floor with free weights" style="background:linear-gradient(180deg,#bfc3c6,#55595d 60%,#2e3134)"></div><span class="rating">4.7</span></div>
        <h3>BARCELONA</h3>
        <p>Sed tristique purus vitae volutpat commodo suscipit amet sed nibh. Proin a ullamcorper sed blandit. Sed tristique purus vitae volutpat commodo suscipit a ullamcorper sed blandit lorem ipsum dolore.</p>
      </article>
      <article class="gym-card">
        <div class="gym-photo"><div class="fill" role="img" aria-label="Group fitness class in a bright studio" style="background:linear-gradient(180deg,#e4e2dc,#a49c92 55%,#6b6a70)"></div><span class="rating">4.7</span></div>
        <h3>BARCELONA</h3>
        <p>Sed tristique purus vitae volutpat commodo suscipit amet sed nibh. Proin a ullamcorper sed blandit. Sed tristique purus vitae volutpat commodo suscipit a ullamcorper sed blandit lorem ipsum dolore.</p>
      </article>
    </div>
    <a class="see-more" href="#">SEE MORE</a>
  </div>
</main>

<section class="partners" aria-label="Partners">
  <svg class="arrow left" width="16" height="28" viewBox="0 0 16 28"><path d="M14 2 3 14l11 12" fill="none" stroke="#9aa0a5" stroke-width="3"/></svg>
  <div class="partner-list">
    <span class="partner"><span class="dot"></span>Brightway Gatherings</span>
    <span class="partner">Fennel Park</span>
    <span class="partner">Eventwell</span>
    <span class="partner">Tidewater Fest</span>
  </div>
  <svg class="arrow right" width="16" height="28" viewBox="0 0 16 28"><path d="M2 2l11 12L2 26" fill="none" stroke="#9aa0a5" stroke-width="3"/></svg>
</section>

<footer class="site-footer">
  <div class="footer-cols">
    <div class="footer-col col-contact">
      <h4>CONTACT</h4>
      <div class="contact-item"><span class="ico"><svg width="14" height="14" viewBox="0 0 14 14"><path d="M3 1l2 3-1.5 1.5a8 8 0 0 0 5 5L10 9l3 2-1 2.5C6 14 0 8 .5 2z" fill="#fff"/></svg></span><span>+44 1632 960418<br>+44 1632 960725</span></div>
      <div class="contact-item"><span class="ico"><svg width="14" height="10" viewBox="0 0 14 10"><rect x="0.5" y="0.5" width="13" height="9" fill="none" stroke="#fff"/><path d="M1 1l6 5 6-5" fill="none" stroke="#fff"/></svg></span><span>support@liftharbor.example<br>hello@liftharbor.example</span></div>
      <div class="contact-item"><span class="ico"><svg width="12" height="14" viewBox="0 0 12 14"><path d="M6 0a5 5 0 0 1 5 5c0 4-5 9-5 9S1 9 1 5a5 5 0 0 1 5-5z" fill="#fff"/></svg></span><span>14 Harbour Lane<br>Dunmere, DM4 7QX</span></div>
    </div>
    <div class="footer-col col-links">
      <h4>USEFUL LINK</h4>
      <ul>
        <li>About Us</li><li>Classes Timetable</li><li>Popular Classes</li><li>Shop Product</li><li>Trainers</li><li>Recent News</li><li>Contact Us</li>
      </ul>
    </div>
    <div class="footer-col col-posts">
      <h4>RECENT POSTS</h4>
      <div class="post"><span class="thumb" role="img" aria-label="Post thumbnail of a training session"></span><p>Pellentesque velit mauris, cursus lectus<time>Oct 12, 2017</time></p></div>
      <div class="post"><span class="thumb" role="img" aria-label="Post thumbnail of a gym workout"></span><p>Pellentesque velit mauris, cursus lectus<time>Oct 12, 2017</time></p></div>
    </div>
    <div class="footer-col">
      <h4>PHOTO GALLERY</h4>
      <div class="gallery" role="img" aria-label="Gallery of gym and event photos">
        <span style="background:#7b5a6e"></span><span style="background:#5d6a7d"></span><span style="background:#8a6d4f"></span>
        <span style="background:#4f6b73"></span><span style="background:#8b4e4a"></span><span style="background:#6a6a72"></span>
        <span style="background:#5b4a60"></span><span style="background:#7a7060"></span><span style="background:#4a5a66"></span>
      </div>
    </div>
  </div>
  <div class="footer-bottom">©2018. All Rights Reserved</div>
</footer>

</body>
</html>
```